Retail Sign for Houseplant Campaign

Please make Portrait style not landscape Sign will measure 3 to 4 foot tall by 22.2inches and place on rolling racks of houseplants for a retail promotion in The Yard Locker. The theme of the promotion will be "Bring your home to life with Houseplants!" Selling points which should be on the sign are Houseplants * improve your mood * reduce fatigue * improve focus. Please put signage in landscape format and include yard locker and verdant makings logo.

Just recovered from covid. Im sorry for the delay

Target Market(s)

People who love plants

Industry/Entity Type

Retail

Colors
00AB8E
00BBA5
67D7C9
C6EFE9
E9F9F6
59FF00
82FF00
B8FF75
E3FFCB
F4FFEA
FFF300
FFF600
FEFA6F
FFFEC7
FFFEE8
FFC000
F8CF3A
FAE287
FDF2CF
FEFAEE

Requirements
Must have
• Must feel energetic and encourage people to buy plants. Should include 1-2 photos and the selling points listed

```html
<!DOCTYPE html>
<html lang="en">
<head>
<meta charset="utf-8">
<title>Houseplants Retail Sign</title>
<link href="https://fonts.googleapis.com/css2?family=Didact+Gothic&family=Fredoka:wght@500;600&display=swap" rel="stylesheet">
<style>
  :root {
    --backdrop: #262626;
    --stone-light: #ffffff;
    --stone-mid: #e6e6e6;
    --headline-orange: #d98b2b;
    --leaf-green: #3b5a2a;
    --sun-yellow: #ecb42a;
    --brand-orange: #f0701f;
  }
  * { margin: 0; padding: 0; box-sizing: border-box; }
  html, body {
    width: 1200px; height: 847px; overflow: hidden;
    background: var(--backdrop);
  }
  .sign {
    position: absolute; left: 129px; top: 134px;
    width: 941px; height: 581px; overflow: hidden;
    background: linear-gradient(180deg, var(--stone-mid) 0%, #ececec 60%, var(--stone-light) 100%);
  }
  .sun-band { position: absolute; inset: 0; }
  .photo {
    position: absolute; left: 650px; top: 0; width: 291px; height: 581px;
    background: linear-gradient(165deg, #6f9a45 0%, #c9a13a 40%, #d8c7a8 65%, #4d6b73 100%);
  }
  .headline {
    position: absolute; left: 38px; top: 42px;
    font-family: "Didact Gothic", sans-serif; font-weight: 400;
    color: var(--headline-orange);
    font-size: 100px; line-height: 85px; letter-spacing: -1px;
  }
  .headline .accent {
    display: block;
    font-family: "Fredoka", sans-serif; font-weight: 600;
    color: var(--leaf-green);
    font-size: 98px; letter-spacing: -2px; margin-top: 4px;
  }
  .brands {
    position: absolute; left: 114px; top: 430px;
    display: flex; align-items: center; gap: 10px;
    font-family: "Fredoka", sans-serif; font-weight: 500;
  }
  .brand-mark { width: 62px; height: 62px; flex: none; }
  .brand-mark.verdant { background: var(--leaf-green); }
  .brand-mark.yard { background: var(--brand-orange); margin-left: 16px; }
  .brand-name { font-size: 26px; line-height: 28px; text-transform: uppercase; }
  .brand-name.verdant { color: var(--leaf-green); }
  .brand-name.yard { color: var(--brand-orange); font-size: 18px; line-height: 21px; }
  .benefits {
    position: absolute; left: 40px; top: 528px;
    display: flex; align-items: center; gap: 12px;
    font-family: "Fredoka", sans-serif; font-weight: 600;
    font-size: 23.5px; color: var(--leaf-green);
  }
  .benefits .divider { width: 3px; height: 30px; background: var(--sun-yellow); }
</style>
</head>
<body>
  <div class="sign">
    <svg class="sun-band" width="941" height="581" viewBox="0 0 941 581">
      <polygon points="600,0 941,0 941,581 675,581" fill="var(--sun-yellow)"/>
    </svg>
    <div class="photo" role="img" aria-label="Smiling woman holding a monstera plant in a large cream pot"></div>

    <h1 class="headline">Bring your<br>home to<br>life with<span class="accent">houseplants!</span></h1>

    <div class="brands">
      <span class="brand-mark verdant"></span>
      <span class="brand-name verdant">Verdant<br>Makings</span>
      <span class="brand-mark yard"></span>
      <span class="brand-name yard">The Yard<br>Locker</span>
    </div>

    <div class="benefits">
      <span>improve your mood</span>
      <span class="divider"></span>
      <span>reduce fatigue</span>
      <span class="divider"></span>
      <span>improve focus</span>
    </div>
  </div>
</body>
</html>
```